Healing Arts Brochure with Simple, Elegant, Zen Design ,

I need to create a brochure for an upcoming event and I have to complete this project in the next few days.
I would like a tri-fold or z fold type of brochure- standard size of 8.5 x 11- both sides with text

i would like the overall design to be simple, elegant and zen .... yet not too plain :-))
I would like the fonts used to be clean and clear and ... easy to read.
I would like the background color to be white/cream or light color
Please do not use too many colors when working with the descriptions of my services or break those sections up too much ... a little is ok.
I don't want the brochure to be busy

I've uploaded the text, my photo, a photo that I will be using on my website, my logo symbol without my name and several logo symbols with my name in different font styles. I am not wed to any of the various font styles of the logo just yet.
TEXT FILE IS UPLOADED

Dear Designers, The design submissions that I'm receiving so far have not been including all 3 pages of text in the brochure. I pulled my text file to update it with the instructions that there are 3 pages of text information that need to be on the brochure. Unfortunately, I'm not able to upload the text file - seems to be a glitch on the ArtMarkly website.. I called for support and they won't get back to me for a couple of hours. That will be around 11:00 am PST in the USA. PLEASE CHECK BACK if you haven't already downloaded the text file. Otherwise, please add the missing information and resubmit your ideas. Thank you!! MR

Target Market(s)

My services target clients in the healing arts.

Industry/Entity Type

Event

Requirements
Must have
• Please include the colors tones of my logo and the sunset photo -golds, oranges, blues
Brochure must include my photo and the sunset photo
Should not have
• Objects like teacups etc. that have nothing to do with my services - thank you kindly
I don't want any other photos or objects on the brochure other than my photo and the sun
Please don't put the tagline in quotes
Please do not make the brochure busy with too many colors in the text.

```html
<!DOCTYPE html>
<html lang="en">
<head>
<meta charset="utf-8">
<title>Maren Rowe – Healing Arts Brochure</title>
<link href="https://fonts.googleapis.com/css2?family=Open+Sans:wght@300;400;600;700&display=swap" rel="stylesheet">
<style>
  :root{
    --bg:#e4e4e4;
    --paper:#ffffff;
    --paper-shade:#eeeeee;
    --orange:#d8731f;
    --blue:#2f5ea8;
    --ink:#3a3a3a;
    --muted:#8a8a8a;
    --white:#ffffff;
    --web:#f6d2b2;
  }
  *{box-sizing:border-box;margin:0;padding:0}
  html,body{width:1200px;height:1000px;overflow:hidden}
  body{
    background:var(--bg);
    font-family:"Open Sans",Arial,sans-serif;
    color:var(--ink);
    display:flex;align-items:center;justify-content:center;
  }
  .brochure{
    display:flex;width:1020px;height:790px;
    box-shadow:0 12px 30px rgba(0,0,0,.18);
  }
  .panel{width:340px;height:100%;position:relative;overflow:hidden}

  /* Panel 1 – profile */
  .panel--profile{background:var(--paper);padding:28px 30px}
  .halo{
    position:absolute;top:-70px;right:-40px;width:330px;height:330px;border-radius:50%;
    background:radial-gradient(circle at 40% 40%,#ffffff 0%,#f1f1f1 60%,#dcdcdc 100%);
  }
  .profile{position:relative;text-align:center}
  .portrait{
    width:120px;height:120px;border-radius:50%;margin:0 auto 12px;
    background:radial-gradient(circle at 50% 45%,#c9a784 0%,#6f7a4c 70%,#3f4a2c 100%);
    border:3px solid var(--white);box-shadow:0 0 0 3px var(--orange);
  }
  .name{font-size:22px;font-weight:700;color:var(--ink)}
  .name small{font-size:11px;color:var(--orange);font-weight:600}
  .credentials{font-size:9.5px;color:var(--muted);line-height:1.45;margin-top:6px}
  .tagline{position:relative;margin-top:20px;font-size:12.5px;font-weight:700;color:var(--orange);line-height:1.4}
  .section-title{font-size:17px;font-weight:700;color:var(--blue);margin:18px 0 8px}
  .body-copy{font-size:11.5px;line-height:1.5;font-weight:600}
  .symptoms-title{font-size:12px;font-weight:700;color:var(--blue);margin:14px 0 6px}
  .symptoms{list-style:none;font-size:10.5px;color:var(--muted);line-height:1.55}
  .symptoms li::before{content:"•";color:var(--ink);margin-right:8px}

  /* Panel 2 – sessions */
  .panel--sessions{background:var(--orange);color:var(--white)}
  .photo{position:relative}
  .photo--hands{
    height:270px;
    background:linear-gradient(135deg,#6d6d6d 0%,#b9aaa0 40%,#e2c5ae 70%,#a89a92 100%);
  }
  .photo-caption{position:absolute;right:20px;top:40px;text-align:right;color:var(--white)}
  .photo-caption .cap-main{font-size:20px;font-weight:300;line-height:1.1}
  .photo-caption .cap-sub{font-size:11px;font-weight:600}
  .sessions-copy{padding:22px 30px;font-size:12px;line-height:1.5;font-weight:600}
  .sessions-copy p+p{margin-top:12px}
  .web{position:absolute;bottom:26px;left:30px;font-size:12px;font-weight:600;color:var(--web)}

  /* Panel 3 – meditation */
  .panel--meditation{background:linear-gradient(180deg,var(--paper) 0%,var(--paper-shade) 100%);padding:30px 30px 0}
  .panel--meditation .section-title{margin-top:0;font-size:18px;line-height:1.2}
  .panel--meditation .body-copy+.body-copy{margin-top:12px}
  .photo--pose{
    position:absolute;left:0;bottom:0;width:340px;height:290px;
    background:linear-gradient(180deg,#8fb7c9 0%,#3f8fb5 45%,#c9c9c9 70%,#9a9a9a 100%);
  }
  .photo--pose .photo-caption{left:24px;right:auto;top:auto;bottom:130px;text-align:left}
</style>
</head>
<body>
<div class="brochure">

  <section class="panel panel--profile">
    <div class="halo"></div>
    <div class="profile">
      <div class="portrait" role="img" aria-label="Portrait photograph of the practitioner"></div>
      <h1 class="name">Maren Rowe <small>CMT, SRP</small></h1>
      <p class="credentials">is a Somatic Resourcing Practitioner, SRP<br>Certified Level II StillRest Teacher<br>Certified Open Path Yoga Teacher<br>Certified Massage Therapist<br>Certified Deep Current Breathwork Facilitator</p>
    </div>
    <p class="tagline">The services that I offer focus on supporting self-empowerment and self-regulation. I am honored to walk with you and support you in your own unique journey home to yourself.</p>
    <h2 class="section-title">Somatic Resourcing</h2>
    <p class="body-copy">Somatic Resourcing is a body-oriented approach to resolving the symptoms of trauma and chronic stress. Sources of trauma are wide-ranging: injuries, accidents, falls, surgeries, physical or sexual abuse, loss of a loved one, childhood neglect or abuse, difficult births, high fever, serious illness, natural disasters, violence and war.</p>
    <h3 class="symptoms-title">The symptoms of unresolved trauma can include:</h3>
    <ul class="symptoms">
      <li>Panic or anxiety (including panic attacks)</li>
      <li>Hyper-vigilance</li>
      <li>Chronic pain of all kinds</li>
      <li>Sleep disorders</li>
      <li>Chronic tension</li>
      <li>Addictions of all kinds</li>
      <li>Migraines</li>
      <li>Gastrointestinal disorders, Dissociation</li>
      <li>And many others</li>
    </ul>
  </section>

  <section class="panel panel--sessions">
    <div class="photo photo--hands" role="img" aria-label="Photograph of hands resting on a client's shoulder during a session">
      <div class="photo-caption"><div class="cap-main">Somatic<br>Resourcing</div><div class="cap-sub">Sessions</div></div>
    </div>
    <div class="sessions-copy">
      <p>Trauma occurs when the instinctual high arousal states of our survival responses (fight, flight and freeze) are unable to discharge, settle and regulate in response to threatening and overwhelming experiences. This energy becomes stuck or frozen as an unresolved memory within the body.</p>
      <p>Somatic Resourcing sessions assist clients to reconnect to their bodies so that frozen energies of trauma are released and resiliency, stability and vitality are restored.</p>
      <p>I integrate both Somatic Resourcing and bodywork techniques in my private practice. The results that I've witnessed in my clients are truly inspiring. Somatic Resourcing is remarkable in its ability to bring healing and relief to the fear, hopelessness and pain of trauma.</p>
    </div>
    <p class="web">www.marenrowe.com</p>
  </section>

  <section class="panel panel--meditation">
    <h2 class="section-title">StillRest &amp; Yoga Nidra Meditation</h2>
    <p class="body-copy">StillRest (Deep Stillness Method) is a modern adaptation of an ancient meditation practice called Yoga Nidra (yogic sleep). StillRest is a research based protocol that provides a systematic path for promoting healing, stress reduction and self-regulation. It is used in the treatment of trauma, P.T.S.D. and many stress related illnesses such as insomnia, chronic pain, anxiety and depression.</p>
    <p class="body-copy">I offer individual sessions of StillRest and personalized instruction in learning Yoga Nidra meditation. The deep relaxation of Yoga Nidra is very restorative as it allows for the release of physical, emotional and mental tension as your body rests in a reclined position. Yoga Nidra facilitates the ability to develop the relaxation response and is one of the most highly effective forms of stress reduction.</p>
    <div class="photo photo--pose" role="img" aria-label="Photograph of a woman in a seated yoga pose beside a pool">
      <div class="photo-caption"><div class="cap-main">StillRest</div><div class="cap-sub">Sessions</div></div>
    </div>
  </section>

</div>
</body>
</html>
```